Mail order Nursery needs banner for promoting perennials that compliment roses.

banner should be 1135 wide x165 tall. We have an existing one displayed but we are not happy with the way it is washed out. Use your creativity to give us something that pops. Would love to see some watercolor or some other form of image other than just words washed across a stock photo. Banner needs to read Perennial Companions for Roses or some variation of that. Colors need to compliment our current theme. You can view the page and banner I want to replace at www.meadowlarkbloomyard.com. The banner we want to replace has been uploaded to the pixel forum file drop box. Thanks for your help and I look forward to seeing what you guys come up with. EDIT: I don't think I was clear enough in by brief. This banner promotes the sale of plants that look good planted with roses. We are getting to many submissions that are using only roses as the backdrop. We are looking for different types of plants that you would grow in your garden to compliment your roses. Thanks for all your hard work.

Target Market(s)

Home owners between 30 and 65

Industry/Entity Type

Nursery

Colors
33a6d7
e667a6

Requirements
Must have
• Text promotion perennials that compliment roses.... does not have to be those exact words but get the point across
Should not have
• Stock Photos with simple text washed across it.

```html
<!DOCTYPE html>
<html lang="en">
<head>
<meta charset="utf-8">
<title>Meadowlark Bloomyard – Perennial Companions for Roses</title>
<link href="https://fonts.googleapis.com/css2?family=Signika:wght@600&family=Fjord+One&family=Open+Sans:wght@400;600&display=swap" rel="stylesheet">
<style>
:root{
  --blue:#33a6d7;
  --pink:#e667a6;
  --ink:#222;
  --muted:#666;
  --rule:#777;
  --light-rule:#e6e6e6;
  --badge-new:#3fae8a;
  --badge-sale:#d9cf45;
  --price:#e24fa6;
  --link:#3a8fc9;
}
*{margin:0;padding:0;box-sizing:border-box}
html,body{width:1200px;height:1000px;overflow:hidden;background:#fff}
body{position:relative;font-family:"Fjord One",Georgia,serif;color:var(--ink)}
h1,h2,h3{font-weight:400}
.banner{position:absolute;overflow:hidden;
  background:linear-gradient(100deg,var(--blue) 0%,#8aa0d6 14%,#d9b7e0 30%,#eea0cc 50%,var(--pink) 65%,#ee9bc0 72%,#f4d9c8 80%)}
.banner::before{content:"";position:absolute;inset:0;
  background:linear-gradient(172deg,transparent 35%,rgba(255,255,255,.35) 48%,transparent 60%)}
.banner-flowers{position:absolute;top:0;right:0;height:100%;
  background:radial-gradient(circle at 70% 45%,#f2f0e8 0 6%,transparent 10%),
  linear-gradient(100deg,rgba(236,150,190,0) 0%,rgba(233,138,44,.85) 14%,#d9621c 38%,#c83a1a 60%,#e7a23a 78%,#6f7a34 100%)}
.banner-title{position:absolute;z-index:1;font-family:"Signika",sans-serif;font-weight:600;color:#fff;
  letter-spacing:-1px;line-height:1;text-shadow:3px 4px 6px rgba(60,40,90,.55);white-space:nowrap}
.banner--top{left:33px;top:51px;width:1135px;height:165px}
.banner--top .banner-flowers{width:380px}
.banner--top .banner-title{left:30px;top:48px;font-size:55px}
.banner--bottom{left:209px;top:767px;width:776px;height:113px}
.banner--bottom .banner-flowers{width:262px}
.banner--bottom .banner-title{left:21px;top:33px;font-size:38px}
.header-rule{position:absolute;left:0;top:267px;width:1200px;height:2px;background:var(--light-rule)}
.subscribe{position:absolute;left:250px;top:300px;width:147px;height:43px;
  background:linear-gradient(90deg,#fbf7ee,#f6e6b5 50%,#f3d98a 70%,#fbf3dc)}
.subscribe-btn{position:absolute;left:26px;top:7px;width:63px;height:21px;background:var(--blue);
  color:#fff;font-size:10px;line-height:21px;text-align:center}
.product{position:absolute;top:303px;width:160px;text-align:center}
.product-photo{position:relative;width:160px;height:120px}
.badge{position:absolute;top:12px;width:47px;height:47px;border-radius:50%;font-family:"Open Sans",sans-serif;
  font-size:8px;font-weight:600;line-height:47px;text-align:center;letter-spacing:.5px;opacity:.9}
.badge span{border-top:1px solid currentColor;border-bottom:1px solid currentColor;padding:1px 0}
.badge--new{left:2px;background:var(--badge-new);color:#fff}
.badge--sale{right:2px;background:var(--badge-sale);color:#222}
.product-actions{list-style:none;font-size:11px;color:#555;line-height:15px;margin-top:1px}
.product-actions li::before{content:"•";margin-right:6px}
.product-name{font-family:"Open Sans",sans-serif;font-size:10px;color:#111;margin-top:9px;letter-spacing:-.2px}
.product-rating{font-size:11px;color:#444;margin-top:15px}
.stars{font-size:7px;color:#bbb;margin-right:2px;vertical-align:1px}
.product-price{font-family:"Open Sans",sans-serif;font-size:10px;margin-top:8px}
.product-price s{color:#888;font-size:8px;margin-right:2px}
.product-price b{color:var(--price);font-weight:600}
.section-heading{position:absolute;left:217px;top:618px;width:760px;display:flex;align-items:center;gap:8px;
  font-family:"Open Sans",sans-serif;font-size:8px;letter-spacing:2px;color:#111}
.section-heading::before,.section-heading::after{content:"";flex:1;height:1px;background:var(--rule)}
.post{position:absolute;left:217px;top:649px;width:180px;font-size:9px;line-height:12px}
.post-meta{font-style:italic;color:var(--muted);font-size:8px}
.post-title{color:var(--link);margin-top:7px;font-size:9px}
.post-excerpt{margin-top:3px;color:#333;font-size:9px}
.post-more{display:block;margin-top:23px;font-style:italic;color:#444;font-size:8px}
.partners{position:absolute;left:217px;top:899px;width:760px;height:110px;border:1px solid #ddd}
.partners-rule{position:absolute;left:0;top:13px;width:100%;height:1px;background:#ddd}
.partner{position:absolute;top:28px}
</style>
</head>
<body>
<header class="banner banner--top">
  <div class="banner-flowers" role="img" aria-label="Photo of orange marigolds, red heleniums and white cosmos in a garden bed"></div>
  <h1 class="banner-title">Perennial Companions for Roses</h1>
</header>
<div class="header-rule"></div>

<aside class="subscribe" role="img" aria-label="Soft floral background behind subscribe button">
  <div class="subscribe-btn">Subscribe</div>
</aside>

<article class="product" style="left:420px">
  <div class="product-photo" role="img" aria-label="Photo of deep pink double roses" style="background:radial-gradient(circle at 40% 40%,#ef5a9a,#c62f6c 60%,#7a2a3a)">
    <div class="badge badge--new"><span>NEW</span></div><div class="badge badge--sale"><span>SALE</span></div>
  </div>
  <ul class="product-actions"><li>Wishlist</li><li>Registry</li></ul>
  <h3 class="product-name">Pink Double Meadow Rose</h3>
  <p class="product-rating"><span class="stars">★★★★★</span>No reviews</p>
  <p class="product-price"><s>$ 28.00</s> <b>$ 15.00</b></p>
</article>
<article class="product" style="left:614px">
  <div class="product-photo" role="img" aria-label="Photo of pink rose shrubs in a landscaped garden" style="background:linear-gradient(180deg,#6f8f4a 0%,#c9679a 45%,#d86ea4 70%,#5c7a3a 100%)">
    <div class="badge badge--new"><span>NEW</span></div><div class="badge badge--sale"><span>SALE</span></div>
  </div>
  <ul class="product-actions"><li>Wishlist</li><li>Registry</li></ul>
  <h3 class="product-name">Pink Meadow Rose</h3>
  <p class="product-rating"><span class="stars">★★★★★</span>No reviews</p>
  <p class="product-price"><s>$ 28.00</s> <b>$ 15.00</b></p>
</article>
<article class="product" style="left:807px">
  <div class="product-photo" role="img" aria-label="Photo of pale blushing pink roses" style="background:radial-gradient(circle at 50% 45%,#f2bcd6,#e58fb8 55%,#4f6a33)">
    <div class="badge badge--new"><span>NEW</span></div><div class="badge badge--sale"><span>SALE</span></div>
  </div>
  <ul class="product-actions"><li>Wishlist</li><li>Registry</li></ul>
  <h3 class="product-name">Blushing Meadow Rose</h3>
  <p class="product-rating"><span class="stars">★★★★★</span>No reviews</p>
  <p class="product-price"><s>$ 28.00</s> <b>$ 15.00</b></p>
</article>

<h2 class="section-heading">LASTEST ADVICE</h2>
<article class="post">
  <p class="post-meta">November 18, 2015 / 0 comments</p>
  <h3 class="post-title">First Post</h3>
  <p class="post-excerpt">This is your store's blog. You can use it to talk about new product launches....</p>
  <span class="post-more">Read more <svg width="10" height="5" viewBox="0 0 10 5"><path d="M0 2.5h9M6.5 0.5 9 2.5 6.5 4.5" stroke="#444" fill="none" stroke-width="1"/></svg></span>
</article>

<section class="banner banner--bottom">
  <div class="banner-flowers" role="img" aria-label="Photo of orange marigolds, red heleniums and white cosmos in a garden bed"></div>
  <h2 class="banner-title">Perennial Companions for Roses</h2>
</section>

<footer class="partners" aria-label="Partner growers">
  <div class="partners-rule"></div>
  <div class="partner" style="left:2px;width:114px;height:62px;border-radius:30px;background:#2e8a58"></div>
  <div class="partner" style="left:147px;width:81px;height:70px;background:#4e8a3a"></div>
  <div class="partner" style="left:264px;top:33px;width:104px;height:32px;background:#cfcfcf"></div>
  <div class="partner" style="left:387px;width:114px;height:50px;background:#efe4d8"></div>
  <div class="partner" style="left:515px;width:114px;height:33px;background:#1f4a52"></div>
  <div class="partner" style="left:643px;width:115px;height:62px;background:#3f8f7a"></div>
</footer>
</body>
</html>
```